Design a Shirt Hang Tag for a brand new streetwear company

We need a hang tag for our apparel. This will be attached and shipper with every shirt, hat, and hoodie. We make streetwear/urban apparel. For a feel of our products see http://loomferal.co

We'd like to see something die cut with a shape that isn't a rectangle.
Looking for a design that embodies "Savage". We are looking for something bold and fun. Our colors usually consist of black. white, and red, but if you feel like doing something else that you feel could fit our brand,go for it. Were savage, we don't want normal.

Target Market(s)

inner city, age 13-29, multi-cultural

Industry/Entity Type

Clothing

Font styles to use
Sans Serif
Other font styles liked:
• artist's choice

Colors
ec1f27
ffffff
000000

Requirements
Must have
• site url: www.loomferal.co
• Band Name: Loom Feral
• Double sided tag
• Die cut design

```html
<!DOCTYPE html>
<html lang="en">
<head>
<meta charset="utf-8">
<title>Loom Feral — Hang Tag</title>
<link rel="stylesheet" href="https://fonts.googleapis.com/css2?family=Rubik:wght@500;700&display=swap">
<style>
  :root {
    --brand-red: #ec1f27;
    --deep-red: #8c0f15;
    --ink-black: #000000;
    --paper-white: #ffffff;
  }
  html, body {
    margin: 0;
    padding: 0;
    width: 1200px;
    height: 2400px;
    overflow: hidden;
    background: var(--paper-white);
  }
  .canvas {
    position: relative;
    width: 1200px;
    height: 2400px;
    overflow: hidden;
    background: var(--paper-white);
    font-family: "Rubik", Arial, sans-serif;
  }
  .tag {
    position: absolute;
    left: 0;
    width: 1200px;
    height: 1120px;
  }
  .tag--front { top: 160px; }
  .tag--back { top: 1312px; }
  .tag__shape {
    position: absolute;
    inset: 0;
    width: 1200px;
    height: 1120px;
    filter: drop-shadow(6px 10px 7px rgba(0, 0, 0, 0.55));
  }
  .tag__wordmark {
    position: absolute;
    left: 0;
    top: 250px;
    width: 1200px;
    margin: 0;
    text-align: center;
    color: var(--paper-white);
    font-weight: 700;
    font-size: 168px;
    line-height: 160px;
    letter-spacing: 4px;
    text-transform: uppercase;
  }
  .tag__wordmark span { display: block; }
  .tag__url {
    position: absolute;
    left: 0;
    top: 375px;
    width: 1200px;
    margin: 0;
    text-align: center;
    color: var(--paper-white);
    font-weight: 500;
    font-size: 50px;
    letter-spacing: 2px;
  }
</style>
</head>
<body>
<main class="canvas">
  <svg width="0" height="0" style="position:absolute" aria-hidden="true">
    <defs>
      <radialGradient id="tag-fill" cx="0.5" cy="0.42" r="0.62">
        <stop offset="0" stop-color="#ff2a33"/>
        <stop offset="0.35" stop-color="#ec1f27"/>
        <stop offset="0.7" stop-color="#9a1118"/>
        <stop offset="1" stop-color="#1a0304"/>
      </radialGradient>
      <path id="tag-outline" d="M45,170 L70,150 L62,140 L95,118 L110,125 L140,100 L160,105 L190,62 L205,75 L225,45 L245,30 L252,50 L262,28 L275,60 L290,110 L300,125 L312,90 L330,55 L345,40 L352,22 L358,45 L372,70 L395,105 L405,115 L420,80 L440,50 L455,38 L468,58 L490,75 L505,70 L530,100 L560,118 L600,115 L628,138 L650,118 L672,150 L700,170 L715,200 L705,230 L718,260 L700,300 L712,330 L695,380 L700,420 L680,460 L690,490 L660,500 L630,515 L600,505 L565,530 L530,545 L500,555 L470,540 L430,525 L400,500 L375,470 L350,430 L338,395 L328,410 L300,450 L270,470 L268,500 L250,555 L220,540 L180,520 L140,515 L100,505 L90,480 L70,420 L55,360 L40,300 L60,270 L40,230 L55,200 Z"/>
    </defs>
  </svg>

  <section class="tag tag--front" aria-label="Hang tag front">
    <svg class="tag__shape" viewBox="0 0 750 700" role="img" aria-label="Die-cut tag with red and black smoky texture">
      <use href="#tag-outline" fill="url(#tag-fill)"/>
      <circle class="tag__hole" cx="365" cy="125" r="6" fill="#ffffff"/>
    </svg>
    <h1 class="tag__wordmark"><span>Loom</span><span>Feral</span></h1>
  </section>

  <section class="tag tag--back" aria-label="Hang tag back">
    <svg class="tag__shape" viewBox="0 0 750 700" role="img" aria-label="Die-cut tag with red and black smoky texture">
      <use href="#tag-outline" fill="url(#tag-fill)"/>
      <circle class="tag__hole" cx="365" cy="125" r="6" fill="#ffffff"/>
    </svg>
    <p class="tag__url">www.loomferal.co</p>
  </section>
</main>
</body>
</html>
```